依頼詳細
明るくポップなイメージでお願いします。
記載事項については添付データを参考にしてください。
イメージ画像も添付してありますが特にこだわりはありませんので、必要事項が入っていればどのようなデザインでも構いません。
年間通して使用するため季節感のないものでお願いします。
記載項目
添付データ参照
希望イメージ
シンプル 複雑
単色 カラフル
暗い 明るい
日常 高級
遊び心 厳粛
未来的 伝統的
女性的 男性的
希望する色
赤系、黄・オレンジ系、無彩色系
納品ファイル
設定なし
補足説明
プレゼントになる景品の画像をご用意いただきたいです。
データ納品後にこちらで差し替える可能性もございますが、そのまま使用する可能性もあるので使用しても問題ない画像を入れてください。
■ 選んだ理由

弊社の企業HPを調べていただいたのだと思いますが、弊社が取り扱っている製品をイラストアイコン化させて掲載されていたことがとても印象強く、社内でも驚きと感動の声があがりました。しっかりと背景を読み込んだうえでご制作いただいたのではないかと思うとお気遣いがとてもうれしく感じました。また、デザインも希望しているものに沿ったデザインで社内で一番好評でした。

■ 提案者全員のお礼・コメント

たくさんのご応募ありがとうございました。本当に素敵なデザインが多くすべての方を当選にしたくなるほど悩みました。裏面までデザインいただいた方もいらっしゃりとても感激いたしました。皆様たくさんのご応募ありがとうございました。

```html
<!DOCTYPE html>
<html lang="ja">
<head>
<meta charset="utf-8">
<title>贅沢グルメプレゼント 大感謝キャンペーン</title>
<link href="https://fonts.googleapis.com/css2?family=M+PLUS+Rounded+1c:wght@500;800;900&family=Noto+Sans+JP:wght@400;500;700;900&family=Noto+Serif+JP:wght@700;900&display=swap" rel="stylesheet">
<style>
:root{
  --red:#e3281e;
  --deep-red:#c81912;
  --orange:#f39a1e;
  --yellow:#ffd23a;
  --cream:#fff6df;
  --ink:#3a2a1c;
  --white:#ffffff;
  --line:#f0a63a;
}
*{margin:0;padding:0;box-sizing:border-box}
html,body{width:811px;height:1200px;overflow:hidden;background:var(--white)}
body{font-family:"Noto Sans JP",sans-serif;color:var(--ink)}
.flyer{position:relative;width:811px;height:1200px;overflow:hidden;background:var(--white)}

.hero{position:absolute;left:0;top:0;width:811px;height:500px;
  background:radial-gradient(ellipse at 50% 40%,#ffe36a 0%,#fbb52a 55%,#f08a14 100%)}
.hero-plate{position:absolute;left:-30px;top:50px;width:740px;height:420px;border-radius:50%;
  background:radial-gradient(ellipse at 50% 45%,#ffffff 0%,#f6f3ec 55%,#e7e0d2 72%,rgba(231,224,210,0) 74%)}
.title{position:absolute;left:0;top:6px;width:811px;text-align:center;
  font-family:"M PLUS Rounded 1c",sans-serif;font-weight:900;font-size:68px;line-height:84px;letter-spacing:1px;color:var(--red);
  text-shadow:4px 0 0 #fff,-4px 0 0 #fff,0 4px 0 #fff,0 -4px 0 #fff,3px 3px 0 #fff,-3px -3px 0 #fff,3px -3px 0 #fff,-3px 3px 0 #fff}
.banner{position:absolute;left:200px;top:96px;width:410px;height:48px;border-radius:6px;background:var(--red);
  color:var(--white);font-family:"M PLUS Rounded 1c",sans-serif;font-weight:900;font-size:34px;line-height:48px;text-align:center;letter-spacing:2px}
.intro{position:absolute;left:220px;top:150px;width:600px;text-align:center;font-weight:500;font-size:16px;line-height:19px;color:var(--ink)}
.intro .lead{color:var(--red);font-weight:900;font-size:17px;line-height:20px}

.prizes{position:absolute;left:26px;top:306px;width:760px;display:flex;justify-content:space-between}
.prize{position:relative;width:240px}
.prize-photo{width:240px;height:110px;border-radius:12px;border:4px solid var(--white)}
.prize-a .prize-photo{background:radial-gradient(circle at 45% 45%,#b44a2e,#6e2614 70%,#3e150a)}
.prize-b .prize-photo{background:radial-gradient(circle at 50% 45%,#ffb8a0,#e86a4c 55%,#b8d6e0 90%)}
.prize-c .prize-photo{background:radial-gradient(circle at 50% 50%,#ffe3ea,#f2a9bb 55%,#e46b7c 90%)}
.prize-tag{position:absolute;left:-6px;top:-8px;width:44px;height:44px;background:var(--red);color:var(--white);
  font-family:"M PLUS Rounded 1c",sans-serif;font-weight:900;font-size:32px;line-height:40px;text-align:center;border:2px solid var(--white)}
.prize-label{margin:-8px auto 0;width:190px;height:76px;border-radius:10px;background:var(--white);position:relative;
  display:flex;flex-direction:column;justify-content:center;align-items:center;
  font-family:"Noto Serif JP",serif;font-weight:900;color:var(--deep-red);font-size:17px;line-height:22px;text-align:center}
.note{position:absolute;right:30px;top:482px;font-size:10px;line-height:14px;color:var(--ink)}

.form{position:absolute;left:34px;top:500px;width:743px;height:560px;border:3px solid var(--line);border-radius:4px;background:var(--white);display:flex;flex-direction:column}
.choose{height:106px;background:linear-gradient(#f7a52a,#f39018);display:flex;align-items:center;justify-content:space-between;padding:0 40px 0 22px}
.choose-text{color:var(--white);font-weight:700;font-size:18px;line-height:30px;white-space:nowrap}
.choose-opts{display:flex;gap:52px;font-family:"M PLUS Rounded 1c",sans-serif;font-weight:900;font-size:64px;line-height:70px;color:var(--red);
  text-shadow:3px 0 0 #fff,-3px 0 0 #fff,0 3px 0 #fff,0 -3px 0 #fff}
.row{display:flex;border-top:2px solid var(--line);font-size:20px;font-weight:500}
.row .cell{padding:16px 18px}
.row-name{height:62px}
.row-name .cell:first-child{width:460px;border-right:2px solid var(--line)}
.row-addr{height:96px}
.row-voice{flex:1}
.row-voice .cell{font-size:13px;padding:8px 18px}

.notice{position:absolute;left:0;top:1068px;width:811px;height:132px;background:var(--cream);padding:8px 34px;font-size:11px;line-height:18px;color:var(--ink)}
.notice h2{font-size:11.5px;font-weight:700}
</style>
</head>
<body>
<div class="flyer">
  <section class="hero">
    <div class="hero-plate" role="img" aria-label="白いお皿とナイフ・フォークの写真"></div>
    <h1 class="title">贅沢グルメプレゼント</h1>
    <p class="banner">大感謝キャンペーン</p>
    <p class="intro">
      いつも弊社ウォーターサーバーを<br>
      ご使用いただき、誠にありがとうございます。<br>
      感謝の気持ちを込めて、<br>
      プレゼントキャンペーンを開催いたします！<br>
      <span class="lead">下記3つからお好きなプレゼントをお選びいただき、<br>抽選で1名様ずつプレゼントいたします。</span><br>
      たくさんのご応募をお待ちしております♪
    </p>
  </section>

  <div class="prizes">
    <div class="prize prize-a">
      <div class="prize-photo" role="img" aria-label="国産牛カルビ肉の写真"></div>
      <span class="prize-tag">A</span>
      <p class="prize-label">国産牛<br>豪華カルビ肉<br>900g</p>
    </div>
    <div class="prize prize-b">
      <div class="prize-photo" role="img" aria-label="海鮮盛り合わせの写真"></div>
      <span class="prize-tag">B</span>
      <p class="prize-label">豪華海鮮<br>贅沢盛り合わせ</p>
    </div>
    <div class="prize prize-c">
      <div class="prize-photo" role="img" aria-label="ケーキ詰め合わせの写真"></div>
      <span class="prize-tag">C</span>
      <p class="prize-label">人気ケーキ<br>詰め合わせ<br>6ピース</p>
    </div>
  </div>
  <p class="note">※画像はイメージです。実際とは異なる場合があります。</p>

  <section class="form">
    <div class="choose">
      <p class="choose-text">ご希望のプレゼントに○をつけてください。<br>クール便で発送します。</p>
      <div class="choose-opts"><span>A</span><span>B</span><span>C</span></div>
    </div>
    <div class="row row-name"><div class="cell">お名前</div><div class="cell">TEL</div></div>
    <div class="row row-addr"><div class="cell">ご住所</div></div>
    <div class="row row-voice"><div class="cell">ご意見やご感想等があればご記入ください。</div></div>
  </section>

  <section class="notice">
    <h2>[注意事項]</h2>
    <p>●記載事項に不備がある場合は無効となります。●ご当選者の発表は賞品の発送をもってかえさせていただきます。●ご応募はお一人様1回限りとさせていただきます。●賞品の内容は予告なく変更となる場合がございます。●賞品の換金・転売はできません。●当選の権利は第三者へ譲渡できません。●ご記入いただいた個人情報は賞品の発送およびサービス向上のためにのみ利用いたします。●発送は国内に限らせていただきます。●天候や交通事情によりお届けが遅れる場合がございます。</p>
  </section>
</div>
</body>
</html>
```